Business Card/ Email Signature Design Project

I am an Interior Designer. I need a business card that looks sophisticated stylish but simple in design. My work covers space design/ interior architecture/ furniture design/ product development & styling.

I have a very specific brief and know mostly what I want. I'm hoping to work with someone who can translate my ideas.

My branding should have a strong focus on my name, the majority of my work is referral based.
I'm keen to keep a monochromatic colour scheme: dark charcoal/ black/ white/ embossing/ silver. I'm not suggesting we use all that I've listed, they are possible ideas at this stage. I will need to be mindful of printing costs an also how I make the design work across, cards, letter heads, email logo and web design.

Theory behind images sent below;
1-Rug Image_(minus boarder) I was thinking this image could be used on the back of the card with my contact details over. I like that the lines are almost hand drawn and start to look free form. It's a subtle contrast to a more formal front of the card with my name.
2_Owen Ratley_I really like the orientation, the proportion of font on the card, the colour and the font. I like the lower case for my name and the upper case for 'Interior Design'. Not sure if it should be 'Interior Designer or Interior Design' at this stage, was leaning towards 'Interior Design'. Was thinking the 'i' and 'd' in my surname could be the colour eg 'silver'?? We can decide on this once we see it.

Look forward to hearing from you.
Cheers,
Noreen Bastoli

Industry/Entity Type

Printing

Logo Text

Noreen Bastoli Interior Design

```html
<!DOCTYPE html>
<html lang="en">
<head>
<meta charset="utf-8">
<title>Noreen Bastoli Interior Design – Business Card</title>
<link rel="stylesheet" href="https://fonts.googleapis.com/css2?family=Montserrat:wght@300;400;600;700&display=swap">
<style>
  :root {
    --page-bg: #efefef;
    --card-bg: #2b2a2a;
    --accent-grey: rgba(128, 128, 128, 0.75);
    --accent-fade: rgba(128, 128, 128, 0);
    --text-white: #ffffff;
    --text-silver: #e2e2e2;
    --card-shadow: rgba(0, 0, 0, 0.28);
  }
  * { margin: 0; padding: 0; box-sizing: border-box; }
  html, body {
    width: 1200px;
    height: 477px;
    overflow: hidden;
    background: var(--page-bg);
    font-family: "Montserrat", Arial, sans-serif;
  }
  .canvas {
    position: relative;
    width: 1200px;
    height: 477px;
  }
  .card {
    position: absolute;
    top: 84px;
    width: 532px;
    height: 306px;
    border-radius: 20px;
    background: var(--card-bg);
    box-shadow: 0 4px 10px var(--card-shadow);
    overflow: hidden;
  }
  .card-front { left: 55px; }
  .card-back { left: 603px; }

  .accent-area {
    position: absolute;
    background: radial-gradient(ellipse at center, var(--accent-grey) 0%, var(--accent-fade) 72%);
  }
  .card-front .accent-top    { left: 10px;  top: 13px;  width: 190px; height: 85px; }
  .card-front .accent-bottom { left: 310px; top: 186px; width: 212px; height: 112px; }
  .card-back .accent-top     { left: 325px; top: 14px;  width: 187px; height: 86px; }
  .card-back .accent-bottom  { left: 9px;   top: 189px; width: 212px; height: 112px; }

  .brand-name {
    position: absolute;
    left: 52px;
    top: 96px;
    font-size: 56px;
    font-weight: 600;
    letter-spacing: 0;
    color: var(--text-white);
    line-height: 1;
    white-space: nowrap;
  }
  .brand-tagline {
    position: absolute;
    left: 54px;
    top: 154px;
    font-size: 24px;
    font-weight: 300;
    letter-spacing: 14px;
    color: var(--text-silver);
    line-height: 1;
    white-space: nowrap;
  }

  .contact-name {
    position: absolute;
    left: 149px;
    top: 81px;
    font-size: 21px;
    font-weight: 600;
    color: var(--text-white);
    white-space: nowrap;
  }
  .contact-list {
    position: absolute;
    left: 147px;
    top: 113px;
    list-style: none;
  }
  .contact-item {
    display: flex;
    align-items: center;
    height: 26.5px;
    font-size: 15px;
    font-weight: 700;
    color: var(--text-white);
    white-space: nowrap;
  }
  .contact-item.address {
    margin-top: 4px;
    font-size: 14px;
    font-weight: 400;
  }
  .contact-icon {
    width: 20px;
    height: 18px;
    margin-right: 13px;
    fill: none;
    stroke: var(--text-white);
    stroke-width: 1.4;
  }
</style>
</head>
<body>
<main class="canvas">

  <section class="card card-front" aria-label="Business card front">
    <div class="accent-area accent-top" role="img" aria-label="Decorative grey geometric pattern"></div>
    <div class="accent-area accent-bottom" role="img" aria-label="Decorative grey geometric pattern"></div>
    <h1 class="brand-name">noreen bastoli</h1>
    <p class="brand-tagline">INTERIOR DESIGN</p>
  </section>

  <section class="card card-back" aria-label="Business card back">
    <div class="accent-area accent-top" role="img" aria-label="Decorative grey geometric pattern"></div>
    <div class="accent-area accent-bottom" role="img" aria-label="Decorative grey geometric pattern"></div>

    <h2 class="contact-name">Noreen Bastoli</h2>
    <ul class="contact-list">
      <li class="contact-item">
        <svg class="contact-icon" viewBox="0 0 20 18" aria-hidden="true">
          <rect x="5.5" y="1" width="9" height="16" rx="1.5"/>
          <line x1="8.5" y1="14.5" x2="11.5" y2="14.5"/>
        </svg>
        0400 555 172
      </li>
      <li class="contact-item">
        <svg class="contact-icon" viewBox="0 0 20 18" aria-hidden="true">
          <rect x="1.5" y="3.5" width="17" height="11" rx="1"/>
          <polyline points="1.5,3.5 10,10 18.5,3.5"/>
        </svg>
        interiors@noreenbastoli.com
      </li>
      <li class="contact-item">
        <svg class="contact-icon" viewBox="0 0 20 18" aria-hidden="true">
          <circle cx="10" cy="9" r="7.5"/>
          <ellipse cx="10" cy="9" rx="3.2" ry="7.5"/>
          <line x1="2.5" y1="9" x2="17.5" y2="9"/>
        </svg>
        www.noreenbastoli.com
      </li>
      <li class="contact-item address">
        <svg class="contact-icon" viewBox="0 0 20 18" aria-hidden="true">
          <path d="M10 17 C6 12 4.5 9.5 4.5 6.8 A5.5 5.5 0 0 1 15.5 6.8 C15.5 9.5 14 12 10 17 Z"/>
          <circle cx="10" cy="6.8" r="2"/>
        </svg>
        P.O Box 274 Elmvale VIC. 3999
      </li>
    </ul>
  </section>

</main>
</body>
</html>
```